Healthcare website - Diabetic Shoes - Elderfund - No Cost

I am looking to upgrade my website. I do not want to use Wordpress, Adobe Muse or another designing program. The code should be easily editable using textpad or VI. After the project is done I want to easily add my custom PHP code.

Features
Creative and Modern Design .
Fully responsive site for use on mobile devices
bootstrap, jquery

My current website is
www.pebblewalkco.com

Target Market(s)

Older people who have diabetes. Target market is +60 years old, but we do have younger people going to the site to help out their parents.

Industry/Entity Type

Healthcare

Coding

Coded - Design and coding required

Number of Pages Required

2 page

Colors

Designer to choose colors to be used in the design.

Requirements
Must have
• The code should be easily editable using textpad or VI. After the project is done I want to easily add my custom PHP code.
• The first page will be the home page and the other page I need is this form.
• https://www.pebblewalkco.com/pebble-walk-co-do-i-qualify.php
Should not have
• I do not want to use Wordpress, Adobe Muse or another designing program.

```html
<!DOCTYPE html>
<html lang="en">
<head>
<meta charset="utf-8">
<title>Pebble Walk Co – Diabetic Shoes Covered by Elderfund</title>
<link href="https://fonts.googleapis.com/css2?family=Josefin+Sans:wght@400;600;700&family=Open+Sans:wght@400;600;700&display=swap" rel="stylesheet">
<style>
:root{
  --blue:#4a76a8;
  --blue-dark:#3d6593;
  --green:#5cb85c;
  --green-bright:#63c25a;
  --ink:#2e4e78;
  --text:#555b63;
  --muted:#8a9099;
  --line:#dfe3e8;
  --footer:#2b2f36;
  --white:#fff;
}
*{box-sizing:border-box;margin:0;padding:0}
html,body{width:1200px;height:3719px;overflow:hidden}
body{font-family:"Open Sans",Arial,sans-serif;color:var(--text);background:var(--white);position:relative}
.heading{font-family:"Josefin Sans","Trebuchet MS",sans-serif;font-weight:600;text-transform:uppercase;letter-spacing:1px;color:var(--ink);text-align:center}

/* top bar */
.topbar{height:35px;background:var(--blue);color:var(--white);font-size:12px;display:flex;align-items:center;padding:0 89px;gap:30px}
.topbar .right{margin-left:auto;display:flex;gap:22px;align-items:center}
.topbar span{display:flex;align-items:center;gap:7px}

/* nav */
.nav{height:74px;display:flex;align-items:center;padding:0 89px;border-bottom:1px solid var(--line)}
.brand{font-family:"Open Sans",sans-serif;font-weight:700;font-size:26px;color:var(--green);display:flex;align-items:center;gap:10px}
.brand i{width:14px;height:14px;border-radius:50%;background:var(--green);display:block}
.menu{margin-left:auto;display:flex;gap:34px;font-size:13px;font-weight:600;color:#3a3f46}
.menu .active{color:var(--green);position:relative}
.menu .active:before{content:"";position:absolute;left:-8px;right:-8px;top:-29px;height:3px;background:var(--green)}

/* hero */
.hero{position:relative;height:493px;background:linear-gradient(120deg,#5a5d5e 0%,#3c3f40 40%,#6b6862 75%,#8a8275 100%)}
.hero-ring{position:absolute;left:171px;top:62px;width:300px;height:300px;border:5px solid var(--blue);border-radius:50%}
.hero-badge{position:absolute;left:233px;top:124px;width:176px;height:176px;border-radius:50%;background:var(--green);display:flex;align-items:center;justify-content:center;font-family:"Josefin Sans",sans-serif;font-weight:700;color:var(--white);font-size:20px;letter-spacing:1px}
.slide-arrow{position:absolute;top:356px;width:24px;height:40px;background:rgba(30,30,30,.7);color:#fff;font-size:14px;display:flex;align-items:center;justify-content:center}
.slide-arrow.prev{left:0}.slide-arrow.next{right:0}

/* intro */
.intro{height:248px;padding-top:80px;text-align:center}
.intro h1{font-size:27px;line-height:32px}
.intro p{font-size:13px;line-height:20px;width:820px;margin:14px auto 0}

/* steps */
.steps{height:434px;background:linear-gradient(rgba(74,118,168,.93),rgba(74,118,168,.93)),linear-gradient(90deg,#6a8eb7,#557fae);padding-top:90px}
.steps h2{color:var(--white);font-size:26px;line-height:30px}
.step-row{display:flex;justify-content:center;gap:80px;margin-top:30px;position:relative}
.step{width:200px;text-align:center;color:var(--white);font-size:12.5px;line-height:18px;position:relative}
.step-icon{width:100px;height:100px;border-radius:50%;background:var(--white);margin:0 auto 16px;display:flex;align-items:center;justify-content:center;position:relative}
.step-icon.on{background:var(--green)}
.step-num{position:absolute;top:-9px;left:41px;width:18px;height:18px;border-radius:50%;background:var(--blue);border:2px solid var(--white);font-size:9px;line-height:14px;color:#fff}
.step-arrow{position:absolute;top:42px;right:-70px}

/* about */
.about{height:451px;position:relative}
.video{position:absolute;left:89px;top:74px;width:384px;height:310px;background:#5e6770;display:flex;align-items:center;justify-content:center}
.play{width:64px;height:64px;border-radius:50%;background:#fff;border:5px solid #cfd6dd;display:flex;align-items:center;justify-content:center}
.about-text{position:absolute;left:575px;top:128px;width:500px}
.about-text h2{text-align:left;font-size:26px}
.about-text p{font-size:12.5px;line-height:20px;margin-top:14px}
.btn{display:inline-block;background:var(--green);color:#fff;font-size:11px;font-weight:700;text-transform:uppercase;padding:10px 20px;margin-top:16px}

/* why */
.why{height:427px;background:linear-gradient(rgba(92,184,92,.92),rgba(92,184,92,.92)),linear-gradient(90deg,#7ccf6f,#4fae4d);padding-top:70px}
.why h2{color:var(--white);font-size:26px}
.accordion{width:632px;margin:12px auto 0}
.acc-item{background:#fff;padding:12px 20px 12px 50px;position:relative;font-size:11px;font-weight:700;text-transform:uppercase;color:#444;margin-bottom:8px;box-shadow:0 2px 6px rgba(0,0,0,.15)}
.acc-item:before{content:"";position:absolute;left:20px;top:12px;width:13px;height:13px;border:1.5px solid #666;border-radius:50%}
.acc-item.open{padding-top:14px;padding-bottom:18px}
.acc-item.open p{font-weight:400;text-transform:none;font-size:12px;line-height:19px;color:#555;margin-top:6px}

/* products */
.products{height:664px;padding-top:80px}
.products h2{font-size:26px}
.cards{position:relative;height:300px;margin-top:38px}
.card{position:absolute;top:0;width:246px;height:290px;border:1px solid var(--line);text-align:center;padding:24px 14px}
.card.lift{box-shadow:0 4px 16px rgba(0,0,0,.18);height:330px;top:-8px;background:#fff}
.card .pic{width:120px;height:150px;margin:0 auto}
.card h3{font-size:13px;font-weight:700;color:#333;margin-top:18px;text-transform:uppercase}
.card p{font-size:11.5px;line-height:16px;margin-top:4px}
.card-actions{display:flex;justify-content:center;gap:6px;margin-top:14px}
.card-actions span{width:30px;height:26px;border:1px solid var(--line);display:flex;align-items:center;justify-content:center}
.card-actions .on{background:var(--blue);border-color:var(--blue)}
.banner{position:absolute;left:89px;top:518px;width:1019px;height:129px;border:5px solid var(--blue);display:flex;align-items:center;justify-content:space-between;padding:0 26px}
.banner .shoes{width:300px;height:85px;border-radius:40px 10px 10px 30px;background:linear-gradient(90deg,#7b7f86,#a5643b)}
.banner .shoes.right{background:linear-gradient(90deg,#3a3a3a,#5b3f3b)}
.banner .mid{text-align:center;font-family:"Josefin Sans",sans-serif;font-weight:700;font-size:18px;color:#222}
.banner .seal{width:58px;height:58px;border-radius:50%;background:#c9ccd2;margin:0 auto 6px}

/* catalog form */
.catalog{height:744px;background:linear-gradient(rgba(255,255,255,.93),rgba(255,255,255,.93)),linear-gradient(90deg,#c9c5bf,#8e8b85);padding-top:152px}
.catalog h2{font-size:26px}
.form{width:918px;margin:28px auto 0;display:grid;grid-template-columns:repeat(3,1fr);column-gap:6px;row-gap:9px}
.field label{display:block;font-size:11px;color:#333;margin-bottom:4px}
.field .input{height:40px;border:1px solid var(--line);background:#fff;font-size:11px;color:var(--muted);padding:0 14px;display:flex;align-items:center;justify-content:space-between}
.form .half{grid-column:span 1}
.row2{grid-column:1 / -1;display:grid;grid-template-columns:1fr 1fr;gap:8px}
.comments{grid-column:1 / -1}
.comments .input{height:110px}
.submit{grid-column:1 / -1;justify-self:center;width:302px;height:36px;background:var(--green);color:#fff;font-size:11px;font-weight:700;text-transform:uppercase;display:flex;align-items:center;justify-content:center;margin-top:0}

/* footer */
.footer{height:149px;background:var(--footer);color:#cfd3d8;position:relative;font-size:10.5px}
.footer .brand{position:absolute;left:89px;top:48px;font-size:22px}
.foot-links{position:absolute;left:514px;top:58px;display:flex;gap:20px;color:#fff}
.copy{position:absolute;left:89px;top:124px;font-size:10px}
.foot-dots{position:absolute;right:270px;top:118px;display:flex;gap:8px}
.foot-dots i{width:16px;height:16px;border-radius:50%;background:#4a8a5a;display:block}
.to-top{position:absolute;right:66px;top:108px;width:26px;height:26px;background:var(--blue);color:#fff;font-size:11px;display:flex;align-items:center;justify-content:center}
</style>
</head>
<body>

<header class="topbar">
  <span><svg width="12" height="12" viewBox="0 0 24 24"><path fill="#fff" d="M6.6 10.8a15 15 0 0 0 6.6 6.6l2.2-2.2c.3-.3.7-.4 1-.2 1.1.4 2.3.6 3.6.6.6 0 1 .4 1 1V20c0 .6-.4 1-1 1A17 17 0 0 1 3 4c0-.6.4-1 1-1h3.5c.6 0 1 .4 1 1 0 1.3.2 2.5.6 3.6.1.3 0 .7-.2 1z"/></svg>1-800-555-0142</span>
  <span><svg width="13" height="12" viewBox="0 0 24 22"><path fill="#fff" d="M2 2h20v14H8l-6 5z"/></svg>Live Chat Office</span>
  <div class="right">
    <svg width="10" height="10"><rect width="10" height="10" rx="2" fill="#fff"/></svg>
    <svg width="10" height="10"><rect width="10" height="10" rx="2" fill="#fff"/></svg>
    <span><svg width="10" height="11" viewBox="0 0 10 11"><circle cx="5" cy="3" r="2.5" fill="#fff"/><path d="M0 11a5 5 0 0 1 10 0z" fill="#fff"/></svg>LOGIN</span>
  </div>
</header>

<nav class="nav">
  <div class="brand"><i></i>Pebble Walk Co</div>
  <div class="menu">
    <span class="active">Home</span>
    <span>Pebble Walk Co: do i qualify</span>
    <span>Why diabetic shoes?</span>
    <span>Shoes</span>
    <span>Products</span>
    <span>Shoe fitter jobs</span>
    <span>FAQ</span>
  </div>
</nav>

<section class="hero" role="img" aria-label="Close-up photograph of a foot in a black and white sneaker stepping on wooden boards">
  <div class="hero-ring"></div>
  <div class="hero-badge">STRIDEWELL</div>
  <div class="slide-arrow prev">&lsaquo;</div>
  <div class="slide-arrow next">&rsaquo;</div>
</section>

<section class="intro">
  <h1 class="heading">Diabetic shoes or sneakers<br>covered by Elderfund</h1>
  <p>No or little out of pocket Cost To You!* Elderfund, and most insurance plans, may cover the cost of one pair of diabetic shoes and three pairs of custom inserts per calendar year. Co-payments, deductibles and some restrictions apply.</p>
</section>

<section class="steps">
  <h2 class="heading">To receive your<br>new therapeutic shoes</h2>
  <div class="step-row">
    <div class="step">
      <div class="step-icon"><span class="step-num">1</span>
        <svg width="34" height="42" viewBox="0 0 34 42"><path d="M2 2h20l10 10v28H2z" fill="none" stroke="#4a76a8" stroke-width="2.5"/><path d="M8 18h18M8 24h18M8 30h12" stroke="#4a76a8" stroke-width="2.5"/></svg>
      </div>
      Fill out an application to see<br>if you qualify.
      <svg class="step-arrow" width="50" height="14"><path d="M0 7h42M36 2l6 5-6 5" fill="none" stroke="#fff" stroke-width="1.5" stroke-dasharray="3 3"/></svg>
    </div>
    <div class="step">
      <div class="step-icon on"><span class="step-num">2</span>
        <svg width="34" height="42" viewBox="0 0 34 42"><rect x="2" y="5" width="30" height="35" fill="none" stroke="#fff" stroke-width="2.5"/><rect x="10" y="1" width="14" height="7" fill="#fff"/><path d="M8 18h18M8 24h18M8 30h12" stroke="#fff" stroke-width="2.5"/></svg>
      </div>
      A prescription will be faxed to<br>your primary physician.
      <svg class="step-arrow" width="50" height="14"><path d="M0 7h42M36 2l6 5-6 5" fill="none" stroke="#fff" stroke-width="1.5" stroke-dasharray="3 3"/></svg>
    </div>
    <div class="step">
      <div class="step-icon"><span class="step-num">3</span>
        <svg width="46" height="26" viewBox="0 0 46 26"><path d="M2 20V6l10 4 8-8 24 14v6H2z" fill="#4a76a8"/></svg>
      </div>
      After the prescription is signed,<br>a certified shoe fitter will fit your new<br>shoes.
      <svg class="step-arrow" width="50" height="14"><path d="M0 7h42M36 2l6 5-6 5" fill="none" stroke="#fff" stroke-width="1.5" stroke-dasharray="3 3"/></svg>
    </div>
    <div class="step">
      <div class="step-icon"><span class="step-num">4</span>
        <svg width="40" height="30" viewBox="0 0 40 30"><path d="M3 16l11 11L37 3" fill="none" stroke="#4a76a8" stroke-width="4"/></svg>
      </div>
      Enjoy your new<br>shoes!
    </div>
  </div>
</section>

<section class="about">
  <div class="video" role="img" aria-label="Video still: line illustration of a shoe fitter measuring a customer's foot">
    <div class="play"><svg width="20" height="22"><path d="M4 2l14 9-14 9z" fill="#4a76a8"/></svg></div>
  </div>
  <div class="about-text">
    <h2 class="heading">About us</h2>
    <p>Pebble Walk Co was created by Harborline Medical Supply to educate clients and prospective shoe fitters about diabetic shoes and the coverage that Elderfund provides. Founded by a Board Certified Pedorthist, the company's mission is to help clients receive properly fitted shoes from qualified healthcare professionals around the United States. Harborline Medical Supply works directly with Elderfund to determine the patient's coverage.</p>
    <span class="btn">Read more</span>
  </div>
</section>

<section class="why">
  <h2 class="heading">Why diabetic shoes?</h2>
  <div class="accordion">
    <div class="acc-item open">How does diabetes cause foot problems?
      <p>Diabetes can cause neuropathy (nerve damage), which reduces feeling in your feet. This makes you less likely to feel the early warning signs of foot problems. Decreased circulation reduces the ability to heal and fight off infection. These two conditions significantly increase the likelihood of foot complications, infection, and ulceration.</p>
    </div>
    <div class="acc-item">Why are properly fitted shoes important?</div>
    <div class="acc-item">How do you know if orthopedic shoes are right for you?</div>
  </div>
</section>

<section class="products" style="position:relative">
  <h2 class="heading">Our Elderfund products</h2>
  <div class="cards">
    <div class="card" style="left:89px">
      <div class="pic" role="img" aria-label="Photo of a handheld TENS unit with electrode pads" style="background:linear-gradient(#4a4d52,#8b9096)"></div>
      <h3>Tens unit</h3><p>A Transcutaneous Electrical Nerve Stimulator.</p>
    </div>
    <div class="card lift" style="left:350px">
      <div class="pic" role="img" aria-label="Photo of a portable electric seat lift cushion" style="background:linear-gradient(#2f3438,#5a6066)"></div>
      <h3>Seat lift</h3><p>Electric-powered portable seat assist can be used</p>
      <div class="card-actions">
        <span><svg width="12" height="11"><path d="M0 1h2l2 7h7l1-5H3" fill="none" stroke="#888"/></svg></span>
        <span class="on"><svg width="12" height="12"><path d="M2 10l8-8M7 2h3v3" fill="none" stroke="#fff" stroke-width="1.5"/></svg></span>
        <span><svg width="12" height="11"><path d="M6 10L1 5a2.5 2.5 0 0 1 5-3 2.5 2.5 0 0 1 5 3z" fill="none" stroke="#888"/></svg></span>
      </div>
    </div>
    <div class="card" style="left:607px">
      <div class="pic" role="img" aria-label="Photo of a lumbar sacral back brace" style="background:linear-gradient(#6fa6d6,#3b4048)"></div>
      <h3>Back brace</h3><p>The Corevia Pro lumbar sacral orthosis immobilizes</p>
    </div>
    <div class="card" style="left:865px">
      <div class="pic" role="img" aria-label="Photo of knee, ankle and wrist braces" style="background:linear-gradient(#1f1f22,#55585e)"></div>
      <h3>Knee, ankle, wrist braces</h3><p>Our knees are susceptible to injuries because they support</p>
    </div>
  </div>
  <div class="banner">
    <div class="shoes" role="img" aria-label="Photo of grey and brown walking shoes"></div>
    <div class="mid"><div class="seal"></div>WOMEN'S SHOES</div>
    <div class="shoes right" role="img" aria-label="Photo of black women's comfort shoes"></div>
  </div>
</section>

<section class="catalog">
  <h2 class="heading">Request a free diabetic shoe catalog</h2>
  <div class="form">
    <div class="field"><label>First Name:</label><div class="input">Enter your first name</div></div>
    <div class="field"><label>Last Name:</label><div class="input">Enter your Last name</div></div>
    <div class="field"><label>Address :</label><div class="input">Enter your Address</div></div>
    <div class="field"><label>City :</label><div class="input">Enter your Phone number</div></div>
    <div class="field"><label>State :</label><div class="input">Enter your State<span>&#9662;</span></div></div>
    <div class="field"><label>Zip :</label><div class="input">Enter your Zip</div></div>
    <div class="field"><label>Phone :</label><div class="input">Enter your City</div></div>
    <div class="field"><label>Best time to Call :</label><div class="input">Enter your time</div></div>
    <div class="field"><label>Email :</label><div class="input">Enter your Email</div></div>
    <div class="row2">
      <div class="field"><label>Primary Insurance :</label><div class="input">Elderfund<span>&#9662;</span></div></div>
      <div class="field"><label>Do you want to check eligibility Online? :</label><div class="input">Yes Check eligibility now<span>&#9662;</span></div></div>
    </div>
    <div class="field comments"><label>Comments :</label><div class="input"></div></div>
    <div class="submit">Request catalog</div>
  </div>
</section>

<footer class="footer">
  <div class="brand"><i></i>Pebble Walk Co</div>
  <div class="foot-links"><span>Terms of Use</span><span>Privacy Policy</span><span>Returns/Exchanges</span><span>* Co-payments, deductibles and some restrictions apply.</span></div>
  <div class="copy">&copy; Copyright Pebble Walk Co - All Rights Reserved</div>
  <div class="foot-dots"><i></i><i></i></div>
  <div class="to-top">&#9650;</div>
</footer>

</body>
</html>
```